Charting 2030 book cover

As part of the Meridian Forum's partnership with the Federal Insight Board, we will be releasing a response report to their World Currents 2030 release. This report will be published as a printed soft cover book(about 100 pgs), as well as an ebook. The size will be approximately 6"x9" with glued binding, so the design could feasibly wrap around.

The report illustrates steps the US needs to take to have a bright and prosperous future in 2030. The world is changing, and we have to prepare for the developing new environment.

Words that come to mind: future, horizon, global, hope, dawn
Concepts that come to mind: sunrise (from space), fork in the road, road map, labyrinth
Updates

I've been asked if we can move the deadline to the previous Friday from the current date of 12/3. Submissions on or before 11/30/2012 are appreciated.

Target Market(s)

intelligence community, think tanks

Industry/Entity Type

Environment

Requirements
Must have
• Name of the report:
Charting 2030: US Policy for a Multipolar Age

Author:
Daniel P. Whitcombe
Long Horizon Project, Harold Lindqvist Center on Global Stability

Logo:
Meridian Forum (uploaded along with branding guidelines)
Should not have
• This should not look like a standard academic report/publication.

```html
<!DOCTYPE html>
<html lang="en">
<head>
<meta charset="utf-8">
<title>Charting 2030 — Cover</title>
<link href="https://fonts.googleapis.com/css2?family=Cinzel:wght@400;600&family=Marcellus+SC&display=swap" rel="stylesheet">
<style>
  :root {
    --top-band: #0d3fd0;
    --header-navy: #17338a;
    --cover-blue: #0b46d6;
    --title-fill: #0a3cc0;
    --title-glow: #7fe3ff;
    --swoosh: #ffffff;
    --logo-ink: #112a78;
    --maze-light: #c9d4f5;
    --maze-mid: #5a72e0;
    --maze-deep: #2a3fb8;
    --white: #ffffff;
  }
  html, body { margin: 0; padding: 0; }
  body { width: 927px; height: 1200px; overflow: hidden; background: var(--cover-blue); }
  .cover {
    position: relative; width: 927px; height: 1200px; overflow: hidden;
    background: var(--cover-blue);
  }
  .cover__band { position: absolute; inset: 0 0 auto 0; height: 48px; background: var(--top-band); }
  .cover__header {
    position: absolute; left: 0; top: 48px; width: 927px; height: 380px;
    background: var(--header-navy);
  }
  .cover__swoosh { position: absolute; left: 0; top: 330px; width: 927px; height: 160px; }
  .cover__title {
    position: absolute; top: 88px; left: 0; width: 100%; margin: 0;
    text-align: center; font-family: "Cinzel", serif; font-weight: 600;
    font-size: 62px; line-height: 70px; letter-spacing: 0;
    color: var(--title-fill);
    -webkit-text-stroke: 1.5px var(--title-glow);
    text-shadow: 0 0 6px var(--title-glow), 0 0 14px var(--title-glow);
  }
  .cover__title span { display: block; }
  .publisher {
    position: absolute; top: 440px; left: 0; width: 100%;
    display: flex; justify-content: center; align-items: center; gap: 18px;
  }
  .publisher__mark { width: 88px; height: 88px; border-radius: 50%; background: var(--logo-ink); }
  .publisher__name {
    font-family: "Cinzel", serif; font-weight: 400; font-size: 58px;
    color: var(--logo-ink); letter-spacing: 0;
  }
  .cover__art {
    position: absolute; left: 48px; top: 590px; width: 831px; height: 500px;
    background:
      radial-gradient(ellipse at 50% 85%, var(--maze-light) 0%, transparent 45%),
      linear-gradient(180deg, var(--maze-light) 0%, var(--maze-mid) 35%, var(--maze-deep) 70%, var(--maze-mid) 100%);
    opacity: .9;
  }
  .cover__author {
    position: absolute; top: 1010px; left: 0; width: 100%; margin: 0;
    text-align: center; font-family: "Marcellus SC", serif;
    font-size: 50px; color: var(--white); letter-spacing: 1px;
  }
  .cover__affiliation {
    position: absolute; top: 1132px; left: 0; width: 100%; margin: 0;
    text-align: center; font-family: "Marcellus SC", serif;
    font-size: 19px; color: var(--white);
  }
</style>
</head>
<body>
<main class="cover">
  <div class="cover__band"></div>
  <div class="cover__header"></div>
  <svg class="cover__swoosh" viewBox="0 0 927 160" aria-hidden="true">
    <path d="M0 70 C 250 10, 650 -10, 927 70 L927 160 L0 160 Z" fill="var(--cover-blue)"/>
    <path d="M55 135 C 300 40, 700 20, 927 100 L927 130 C 700 50, 320 60, 55 135 Z" fill="var(--swoosh)"/>
  </svg>
  <h1 class="cover__title">
    <span>Charting 2030:</span>
    <span>US Policy</span>
    <span>for a Multipolar Age</span>
  </h1>
  <div class="publisher">
    <div class="publisher__mark"></div>
    <div class="publisher__name">Meridian Forum</div>
  </div>
  <div class="cover__art" role="img" aria-label="Glowing blue labyrinth seen from above with a lone figure standing at its lit entrance"></div>
  <p class="cover__author">Daniel P. Whitcombe</p>
  <p class="cover__affiliation">Long Horizon Project, Harold Lindqvist Center on Global Stability</p>
</main>
</body>
</html>
```